SCL Business Card

A double sided business card based on your "Strideway Clinic Ltd" Logo. To use the "SCL" logo on 1 side and the full company logo on the reverse.

Detials to be included:

Name: Megan Talbot
Postion: Consultant Orthotist & Expert Witness
T: +44 (0) 7845 203917
F: +44 (0) 7468 5021

```html
<!DOCTYPE html>
<html lang="en">
<head>
<meta charset="utf-8">
<title>Strideway Clinic Ltd – Business Card</title>
<link rel="stylesheet" href="https://fonts.googleapis.com/css2?family=Open+Sans:wght@400;600;700&display=swap">
<style>
  :root {
    --navy: #0d3a6e;
    --grey: #8c8c8e;
    --text-grey: #6f6f72;
    --card-white: #ffffff;
    --backdrop: #ecebe8;
    --rule: #b9b9bb;
  }
  * { margin: 0; padding: 0; box-sizing: border-box; }
  html, body { width: 1200px; height: 720px; overflow: hidden; }
  body {
    background: var(--backdrop);
    font-family: "Open Sans", Arial, sans-serif;
    display: flex;
    align-items: center;
    justify-content: center;
    gap: 40px;
  }
  .card {
    width: 540px;
    height: 309px;
    position: relative;
    box-shadow: 0 6px 18px rgba(0,0,0,0.18);
  }
  .card-front { background: var(--card-white); }
  .card-back {
    background: var(--navy);
    display: flex;
    align-items: center;
    justify-content: center;
  }

  /* front: company identity */
  .identity {
    position: absolute;
    left: 38px;
    top: 40px;
    display: flex;
    align-items: center;
  }
  .identity-mark {
    width: 58px;
    height: 58px;
    background: var(--navy);
  }
  .identity-divider {
    width: 1px;
    height: 66px;
    background: var(--rule);
    margin: 0 16px;
  }
  .company-name {
    font-weight: 600;
    font-size: 25px;
    line-height: 1.1;
    color: var(--navy);
    text-transform: uppercase;
    letter-spacing: 0.5px;
  }
  .tagline {
    margin-top: 6px;
    padding-top: 4px;
    border-top: 1px solid var(--rule);
    font-size: 8.5px;
    letter-spacing: 0.6px;
    text-transform: uppercase;
    color: var(--navy);
  }

  /* front: person */
  .person {
    position: absolute;
    right: 36px;
    top: 118px;
    text-align: right;
  }
  .person-name {
    font-weight: 700;
    font-size: 16px;
    color: var(--navy);
  }
  .person-role {
    font-size: 12.5px;
    line-height: 1.3;
    color: var(--text-grey);
  }

  /* front: contact */
  .contact {
    position: absolute;
    left: 42px;
    bottom: 34px;
    list-style: none;
    font-size: 12px;
    color: var(--text-grey);
  }
  .contact li {
    display: flex;
    align-items: center;
    gap: 7px;
    line-height: 21px;
  }
  .contact svg { width: 11px; height: 11px; fill: var(--navy); flex: none; }
  .contact .address { margin-top: 12px; padding-left: 0; }

  /* back: monogram */
  .monogram {
    display: flex;
    align-items: center;
    gap: 16px;
  }
  .monogram-square {
    width: 44px;
    height: 44px;
    background: var(--grey);
  }
  .monogram-text {
    font-weight: 600;
    font-size: 62px;
    letter-spacing: 6px;
    color: var(--card-white);
  }
</style>
</head>
<body>

  <section class="card card-front" aria-label="Business card front">
    <div class="identity">
      <div class="identity-mark"></div>
      <div class="identity-divider"></div>
      <div class="identity-words">
        <div class="company-name">Strideway<br>Clinic Ltd</div>
        <div class="tagline">Excellence in Medical Legal Reporting</div>
      </div>
    </div>

    <div class="person">
      <div class="person-name">Megan Talbot</div>
      <div class="person-role">Consultant Orthotist<br>Expert Witness</div>
    </div>

    <ul class="contact">
      <li>
        <svg viewBox="0 0 16 16" aria-hidden="true"><path d="M3.6 1.2l2.3 2.6-1.3 1.8c.9 2 2.4 3.5 4.4 4.5l1.8-1.3 2.6 2.3-1.4 2.6C6.9 13.4 2.6 9.1 1 3z"/></svg>
        +44 (0) 7845 203917
      </li>
      <li>
        <svg viewBox="0 0 16 16" aria-hidden="true"><path d="M4 1h7v4H4zM2 6h12v6h-2v3H4v-3H2zM5 10v4h6v-4z"/></svg>
        +44 (0) 7468 5021
      </li>
      <li>
        <svg viewBox="0 0 16 16" aria-hidden="true"><path d="M1 3h14v10H1zM2.5 4.5L8 9l5.5-4.5v-.1H2.5z"/></svg>
        megan@stridewayclinic.co.uk
      </li>
      <li class="address">18 Ashcombe Road, Kingsbridge, Surrey, KT7 4PR</li>
    </ul>
  </section>

  <section class="card card-back" aria-label="Business card back">
    <div class="monogram">
      <div class="monogram-square"></div>
      <div class="monogram-text">SCL</div>
    </div>
  </section>

</body>
</html>
```